Stationary Design to Complement our Website

We would like template designed for word documents that we can use for headed paper. The template should complement the style of our website & incorporate our existing logo. https://www.velmorantravel.com/

The header and footer design should be sperate PNG or JPEG files that we can copy and paste into word header and footers. They should work on A4 & letter sized papers.

Note the main web colours are as follows:

Black
HEX code #2b2c2b
C=71 M=64 Y=64 K=65
RGB 43,44,43

Green
HEX code #116c49
C=88 M=33 Y=82 K=24
RGB 17,108,73

Current fonts are ALEO & Gilroy.

Fonts and colours in new design don't have to match website exactly but should be complementary.

Font styles to use
Serif

Requirements
Must have
• a simple design that complements our website.
Some kind of graphic on the top & some sort of graphic on the bottom. Not just plain logo on top.
designs that incorporate the clouds might look good
Can also incorporate 5* rate harbor rating
Should not have
• no photographs included on the design

```html
<!DOCTYPE html>
<html lang="en">
<head>
<meta charset="utf-8">
<title>Velmoran Travel Letterhead</title>
<link rel="stylesheet" href="https://fonts.googleapis.com/css2?family=Cinzel:wght@400&family=Source+Sans+3:wght@400&family=Montserrat:wght@400&display=swap">
<style>
  :root {
    --backdrop: #808080;
    --paper: #f6f3f3;
    --ink: #141414;
    --text: #555555;
    --green: #116c49;
    --watermark: #e5e7e5;
    --sign-tone: #dcdcdc;
  }
  * { margin: 0; padding: 0; box-sizing: border-box; }
  html, body { width: 1072px; height: 1200px; overflow: hidden; }
  body { background: var(--backdrop); position: relative; }

  .letterhead {
    position: absolute; left: 208px; top: 125px;
    width: 682px; height: 961px;
    background: var(--paper);
    box-shadow: 1px 1px 2px rgba(0,0,0,0.35);
    overflow: hidden;
  }

  .brand-dot {
    position: absolute; left: 210px; top: 78px;
    width: 28px; height: 28px; border-radius: 50%;
    background: var(--green);
  }
  .brand {
    position: absolute; left: 246px; top: 84px;
    font-family: "Cinzel", serif; color: var(--ink);
  }
  .brand-name {
    font-size: 36px; letter-spacing: 6px; line-height: 45px; white-space: nowrap;
  }
  .brand-name--first { padding-left: 6px; }

  .watermark {
    position: absolute; left: 156px; top: 300px;
    width: 360px; height: 360px; border-radius: 50%;
    background: var(--watermark);
  }

  .letter {
    position: absolute; left: 67px; top: 0; width: 549px;
    font-family: "Source Sans 3", sans-serif; color: var(--text);
  }
  .greeting { position: absolute; top: 264px; font-size: 18px; white-space: nowrap; }
  .body { position: absolute; top: 322px; width: 549px; }
  .body p {
    font-size: 10.5px; line-height: 16.4px; text-align: justify;
    margin-bottom: 16.4px;
  }
  .closing { position: absolute; top: 667px; font-size: 10.5px; }
  .signature {
    position: absolute; top: 705px; left: 0; width: 88px; height: 36px;
    background: linear-gradient(90deg, var(--paper), var(--sign-tone), var(--paper));
    border-radius: 4px;
  }

  .contact {
    position: absolute; top: 853px;
    font-family: "Montserrat", sans-serif; color: var(--text);
    font-size: 9.6px; line-height: 12.5px;
  }
  .contact-icon { display: block; margin-bottom: 10px; }
  .contact-address { left: 65px; }
  .contact-address .contact-icon { margin-left: 27px; margin-bottom: 7px; }
  .contact-phone { left: 304px; }
  .contact-phone .contact-icon { margin-left: 19px; }
  .contact-web { left: 510px; }
  .contact-web .contact-icon { margin-left: 37px; }
</style>
</head>
<body>
  <main class="letterhead">
    <div class="watermark" aria-hidden="true"></div>

    <div class="brand-dot" aria-hidden="true"></div>
    <header class="brand">
      <div class="brand-name brand-name--first">VELMORAN</div>
      <div class="brand-name">TRAVEL</div>
    </header>

    <section class="letter">
      <p class="greeting">Dear Mr. Hollis,</p>
      <div class="body">
        <p>Lorem ipsum dolor sit amet, consectetur adipiscing elit. Donec orci purus, luctus vitae dignissim eu, iaculis sed purus. Vivamus faucibus, ipsum nec aliquet viverra, leo mauris condimentum ligula, sit amet sagittis enim ligula quis arcu. Nam egestas tortor id nisi porttitor mattis. In tortor ante, ultricies in suscipit a, tempus non massa. Vivamus et auctor mi. Fusce vel massa nulla. Phasellus nec eros mauris, et scelerisque orci.</p>
        <p>Donec malesuada orci vitae nulla accumsan porta a id massa. Quisque accumsan iaculis magna sit amet fringilla. Maecenas consequat, magna eget tincidunt semper, odio nibh rutrum mi, id feugiat ante nisi eu risus. Vestibulum nunc orci, rhoncus a placerat in, ultricies in mi. Cras mattis varius eros, vel fringilla nisi suscipit eget. Quisque scelerisque sagittis nulla at porttitor.</p>
        <p>Sed id augue vitae urna euismod commodo aliquet a quam. Pellentesque arcu velit, cursus et malesuada ut, consequat et diam. Nullam erat sem, rhoncus id ullamcorper vitae, rhoncus et arcu. In ultricies ultricies nulla, ut rutrum nisi iaculis at. Donec eu magna a metus ornare faucibus. Fusce aliquet faucibus ultricies. Morbi semper, est id tincidunt gravida, sem arcu adipiscing lacus, ac bibendum nulla leo eu purus. Quisque nec diam sed risus consectetur a ccumsan quis quis nibh. Vestibulum id purus lorem.</p>
        <p>It is a long established fact that a reader will be distracted by the readable content of a page when looking at its layout. The point of using Lorem Ipsum is that it has a more-or-less normal distribution of letters, as opposed to using 'Content here, content here', making it look like readable English. Many desktop publishing packages</p>
      </div>
      <p class="closing">Sincerely,</p>
      <div class="signature" role="img" aria-label="Handwritten signature of the sender"></div>
    </section>

    <footer>
      <div class="contact contact-address">
        <svg class="contact-icon" width="28" height="28" viewBox="0 0 28 28" aria-hidden="true">
          <circle cx="14" cy="14" r="14" fill="var(--green)"/>
          <path d="M14 6.5a5 5 0 0 0-5 5c0 3.8 5 9.5 5 9.5s5-5.7 5-9.5a5 5 0 0 0-5-5z" fill="#fff"/>
          <circle cx="14" cy="11.5" r="1.9" fill="var(--green)"/>
        </svg>
        4120 Alder Crest Road<br>Juneau, Alaska 99801
      </div>
      <div class="contact contact-phone">
        <svg class="contact-icon" width="28" height="28" viewBox="0 0 28 28" aria-hidden="true">
          <circle cx="14" cy="14" r="14" fill="var(--green)"/>
          <path d="M10.2 7.5l2.2 2.6-1.3 1.7c.8 1.9 2.2 3.3 4.1 4.1l1.7-1.3 2.6 2.2-1.2 2.3c-4.9-.3-9.3-4.7-9.6-9.6z" fill="#fff"/>
        </svg>
        555-014-2870<br>555-019-6341
      </div>
      <div class="contact contact-web">
        <svg class="contact-icon" width="28" height="28" viewBox="0 0 28 28" aria-hidden="true">
          <circle cx="14" cy="14" r="14" fill="var(--green)"/>
          <rect x="7.5" y="9.5" width="13" height="9" rx="1" fill="#fff"/>
          <path d="M7.8 10l6.2 4.6 6.2-4.6" fill="none" stroke="var(--green)" stroke-width="1.2"/>
        </svg>
        info@velmorantravel.com<br>www.velmorantravel.com
      </div>
    </footer>
  </main>
</body>
</html>
```